Business Card Design

wig manufacturer
I would like something very upscale.highend looking
maybe mat chrome card with shiney chrome
or something like the Quorix business card very clean and simple white with the logo in silver
Target Market(s)
upscale women
Industry/Entity Type
Business
Contact Information for Business Card
OUR LOGO
company name:Marisol Tresses
48E52Street Dennis Holcroft
New York,N.Y 10036
Tel:646-5817730
1800-4369185
email:hairloft@zentrimail.com
website:Marisoltresses.com
Look and feel
Each slider illustrates characteristics of the customer's brand and the style your logo design should communicate.

```html
<!DOCTYPE html>
<html lang="en">
<head>
<meta charset="utf-8">
<title>Marisol Tresses — Business Card</title>
<link rel="stylesheet" href="https://fonts.googleapis.com/css2?family=Josefin+Sans:wght@300;400;600&display=swap">
<style>
  :root {
    --backdrop: #e9e6e2;
    --card: #fdfdfc;
    --ink: #1f1f1f;
    --ink-soft: #4a4a4a;
    --silver: #a9abae;
    --silver-light: #d3d5d8;
  }
  html, body {
    margin: 0;
    padding: 0;
    width: 796px;
    height: 1200px;
    overflow: hidden;
    background: var(--backdrop);
  }
  .canvas {
    position: relative;
    width: 796px;
    height: 1200px;
    font-family: "Josefin Sans", sans-serif;
  }
  .card {
    position: absolute;
    left: 178px;
    top: 215px;
    width: 440px;
    height: 770px;
    background: var(--card);
    box-shadow: 0 2px 10px rgba(0,0,0,0.12);
    display: flex;
    flex-direction: column;
    align-items: center;
    text-align: center;
    color: var(--ink);
  }
  .brand-mark {
    margin-top: 120px;
    display: flex;
    align-items: center;
    gap: 14px;
  }
  .brand-square {
    width: 46px;
    height: 46px;
    background: linear-gradient(135deg, var(--silver-light), var(--silver));
  }
  .brand-name {
    font-size: 30px;
    font-weight: 600;
    color: var(--silver);
    letter-spacing: 0.5px;
  }
  .holder-name {
    margin: 150px 0 0;
    font-size: 30px;
    font-weight: 400;
    letter-spacing: 0.5px;
  }
  .holder-title {
    margin-top: 10px;
    font-size: 11px;
    font-weight: 400;
    letter-spacing: 6px;
    color: var(--ink-soft);
  }
  .contact {
    margin-top: 60px;
    font-size: 19px;
    font-weight: 400;
    line-height: 1.75;
    font-style: normal;
  }
  .contact p { margin: 0; }
</style>
</head>
<body>
<main class="canvas">
  <section class="card">
    <div class="brand-mark">
      <span class="brand-square"></span>
      <span class="brand-name">Marisol Tresses</span>
    </div>
    <h1 class="holder-name">Marisol Tresses</h1>
    <div class="holder-title">PRESIDENT</div>
    <address class="contact">
      <p>48E52 Street Dennis Holcroft New York</p>
      <p>N.Y 10036</p>
      <p>T: 646-5817730; 1800-4369185</p>
      <p>E :hairloft@zentrimail.com</p>
      <p>www.Marisoltresses.com</p>
    </address>
  </section>
</main>
</body>
</html>
```